Personal Business card and maybe logo or graphic?

I would like a card to give out like you would a business card, however I am not promoting a business, it is just for my personal details.

I have no brand and no logo to worry about.

I would like some images or a logo of some kind or a graphic so the card has some excitement about it.

I am happy if you wish to create a logo/graphic that represents my name, I have seen someone with just their initials as a graphic so for me PH, however I am happy for you to create anything you wish, it does not have to relate to me just make the card look fun and still professional.

Please use the details

Peter Hadley

Ashcombe Lodge
9 The Mews
Fern Close
Bournemouth
Dorset
BH4 2QT

+44 (0)7812 604258
peter@hadleypost.example
linkedin.example/in/hadleypeter

looking for a mix between fun, fresh , young whilst being professional

I am new to this and am looking for you to guide me through the process please ask questions and ideas

I am just tidying up my brief as I am starting to understand more. hope it has not confused anyone
Updates

Reason: I have not had time to review or comment due to personal issues sorry

Hi,

to help would you be so kind as to use these sample details on the card

I am uk based and a few designs have us details which look different

Peter Hadley

Ashcombe lodge

9 The Mews

Fern Close

Bournemouth

Dorset

BH4 2QT

+44 (0)7812 604258

peter@hadleypost.example

many thanks hope that is ok and not too much trouble!

regards

Pim

My are of expertise is IT management / IT Consultancy, incase you wish to incorporate any graphics

My job was that of CIO (Chief Information Officer) or another term is Head of IT

just advising incase this gives any assistance as one designer has asked s may be useful to others

thanks                                   

just thought I have had a look and the UK size for a business card seems to be as per below

I thought I would mention as I guess the US size may be different and other countries too

I found these sizes on Cardforge but guess most companies will be similar

that said maybe you can advise me

I have no idea what cardforge is like so not sure where to get cards made, will figure that out later I guess but I assume dimensions are important for the design

thanks

 

Document Trim Size    

            Horizontal        

        85 x 55 mm           

1004 x 650 pixels           

            Vertical        

        55 x 85 mm           

650 x 1004 pixels           

        Full Bleed Size    

            Horizontal        

        88 x 58 mm           

1039 x 685 pixels           

            Vertical        

        58 x 88 mm           

685 x 1039 pixels           

 many thanks

Target Market(s)

Professional and personal contacts

Industry/Entity Type

Business

```html
<!DOCTYPE html>
<html lang="en">
<head>
<meta charset="utf-8">
<title>Peter Hadley – Business Card</title>
<link rel="stylesheet" href="https://fonts.googleapis.com/css2?family=Barlow+Semi+Condensed:wght@300;400&display=swap">
<style>
  :root {
    --sky: #8fd0f5;
    --paper: #ffffff;
    --ink-blue: #2aa6e0;
    --ink-white: #ffffff;
  }
  * { margin: 0; padding: 0; box-sizing: border-box; }
  html, body {
    width: 1200px;
    height: 765px;
    overflow: hidden;
    background: var(--paper);
  }
  .card {
    position: relative;
    width: 1200px;
    height: 765px;
    font-family: "Barlow Semi Condensed", "Arial Narrow", sans-serif;
    background: var(--paper);
  }
  .card__panel {
    position: absolute;
    left: 0;
    top: 0;
    width: 580px;
    height: 765px;
    background: var(--sky);
  }
  .monogram {
    position: absolute;
    left: 58px;
    top: 100px;
    color: var(--ink-white);
    font-weight: 300;
    font-size: 300px;
    line-height: 1;
    letter-spacing: -4px;
  }
  .contact {
    position: absolute;
    left: 42px;
    top: 540px;
    list-style: none;
    color: var(--ink-white);
    font-weight: 300;
    font-size: 33px;
    line-height: 46px;
  }
  .identity {
    position: absolute;
    right: 82px;
    top: 222px;
    text-align: right;
    color: var(--ink-blue);
  }
  .identity__name {
    font-weight: 300;
    font-size: 56px;
    line-height: 1;
    margin-bottom: 52px;
  }
  .address {
    font-style: normal;
    font-weight: 300;
    font-size: 31px;
    line-height: 61px;
  }
</style>
</head>
<body>
  <main class="card">
    <section class="card__panel">
      <div class="monogram">PH</div>
      <ul class="contact">
        <li>+44 (0)7812 604258</li>
        <li>peter@hadleypost.example</li>
        <li>linkedin.example/in/hadleypeter</li>
      </ul>
    </section>
    <section class="identity">
      <h1 class="identity__name">Peter Hadley</h1>
      <address class="address">
        Ashcombe Lodge<br>
        9 The Mews<br>
        Fern Close<br>
        Bournemouth<br>
        Dorset<br>
        BH4 2QT
      </address>
    </section>
  </main>
</body>
</html>
```